依頼詳細
楢井マッサージ治療院のパンフレットのリニューアルデザインを依頼させて頂きます。基本的には、既存のパンフレットに掲載している情報を新しいパンフレットにして頂きたいと思っています。カラー等もホームページを参考にしてください。
サイズ
A4
ページ数
4ページ
希望イメージ
シンプル 複雑
単色 カラフル
暗い 明るい
日常 高級
遊び心 厳粛
未来的 伝統的
女性的 男性的
希望する色
黄・オレンジ系
納品ファイル
設定なし
補足説明
ホームページ(http://naraimassage-example.com/)もご参考下さい。
・写真素材を添付にてご用意させて頂きました。
・文言全般につきましては、添付PDFを参照の上、ウェブサイトのものを利用ください。
・技術情報の文言につきましては、新しく添付させて頂きましたので、ご利用ください。
依頼金額を10800円程追加させて頂きました。ご検討下さい。
■ 選んだ理由

提供素材である写真のトーンに統一感がなく、また情報量が多い上、老若男女偏りがなく、読みやすく、高級感や信頼感、そして安心感があるデザインといった難しい要望にも関わらず、患者さんの視点に立ち、かつ私たちの要望を的確に汲み取って頂き、誠心誠意ベストを尽くしてくださったことから、この作品を選ばさせて頂きました。

■ 提案者全員のお礼・コメント

この度は、当院のパンフレットデザインのコンペに参加頂き誠にありがとうございます。写真のトーンに統一感がなく、情報量も多かったため、難しい要望の中、様々な工夫とご提案頂き誠に感謝しております。今後もコンペ形式で様々な印刷物やウェブデザインのリニューアルを考えておりますので、また是非ご提案頂けますよう宜しくお願い申し上げます。

```html
<!DOCTYPE html>
<html lang="ja">
<head>
<meta charset="utf-8">
<title>楢井マッサージ治療院 パンフレット</title>
<link rel="stylesheet" href="https://fonts.googleapis.com/css2?family=Noto+Serif+JP:wght@400;600&family=Noto+Sans+JP:wght@400;500&display=swap">
<style>
  :root{
    --paper:#ffffff;
    --backdrop:#f4f3f1;
    --cover:#f5d583;
    --cover-deep:#e9c161;
    --ink:#3a3330;
    --ink-soft:#6d625c;
    --mark-bg:#f6ece2;
    --accent:#8a6a3c;
    --flower:#d6c548;
  }
  *{margin:0;padding:0;box-sizing:border-box}
  html,body{width:846px;height:1200px;overflow:hidden;background:var(--backdrop)}
  .canvas{position:relative;width:846px;height:1200px;overflow:hidden}
  .spread{
    position:absolute;left:0;top:0;width:1200px;height:846px;
    transform-origin:0 0;transform:translate(0,1200px) rotate(-90deg);
    font-family:"Noto Sans JP",sans-serif;color:var(--ink);
  }
  .cover{
    position:absolute;left:57px;top:42px;width:621px;height:762px;
    background:var(--cover);
  }
  .cover-mark{
    position:absolute;left:200px;top:88px;width:220px;height:220px;
    background:var(--mark-bg);display:flex;align-items:center;justify-content:center;
    font-family:"Noto Serif JP",serif;font-weight:600;font-size:19px;color:var(--accent);
    text-align:center;line-height:1.5;padding:20px;
  }
  .cover-tagline{position:absolute;left:0;right:0;top:350px;text-align:center;
    font-family:"Noto Serif JP",serif;font-size:15px;letter-spacing:.2em;color:var(--ink)}
  .cover-title{position:absolute;left:0;right:0;top:382px;text-align:center;
    font-family:"Noto Serif JP",serif;font-weight:600;font-size:40px;letter-spacing:.08em;color:var(--ink)}
  .cover-contact{position:absolute;left:0;right:0;top:590px;text-align:center;
    font-family:"Noto Serif JP",serif;font-size:14px;line-height:1.9;color:var(--ink)}
  .cover-contact .tel{font-size:17px;letter-spacing:.06em}

  .inner{
    position:absolute;left:678px;top:42px;width:466px;height:762px;background:var(--paper);
    padding:36px 34px;
  }
  .inner-head{display:flex;align-items:center;gap:14px;margin-bottom:22px}
  .inner-head .emblem{width:34px;height:34px;border-radius:50%;background:var(--cover-deep)}
  .inner-head h2{font-family:"Noto Serif JP",serif;font-weight:600;font-size:17px;letter-spacing:.1em}
  .section{margin-bottom:18px}
  .section h3{font-size:11px;font-weight:500;color:var(--accent);margin-bottom:5px;letter-spacing:.06em}
  .section p{font-size:9.5px;line-height:1.85;color:var(--ink-soft)}
  .lower{display:flex;gap:18px;margin-top:14px}
  .lower .texts{flex:1}
  .flower-photo{width:150px;height:150px;flex:none;
    background:radial-gradient(circle at 50% 50%,#e6dc6a 0%,var(--flower) 45%,#a9a34a 100%)}
</style>
</head>
<body>
<div class="canvas">
  <div class="spread">
    <section class="cover">
      <div class="cover-mark">楢井マッサージ治療院</div>
      <p class="cover-tagline">揉み療法による体のケア</p>
      <h1 class="cover-title">楢井マッサージ治療院</h1>
      <div class="cover-contact">
        <p>緑ヶ丘県若葉市本町 2-14-7</p>
        <p class="tel">TEL 0120-55-0198</p>
        <p>http://naraimassage-example.com/</p>
      </div>
    </section>

    <section class="inner">
      <div class="inner-head">
        <span class="emblem" aria-hidden="true"></span>
        <h2>想いをこめた治療</h2>
      </div>
      <div class="section">
        <h3>当院について</h3>
        <p>一人ひとりの体の声に耳を傾け、丁寧な手技で日々の疲れや痛みをやわらげます。ご家族皆さまが安心して通える治療院を目指しています。</p>
      </div>
      <div class="section">
        <h3>揉み療法とは</h3>
        <p>筋肉のこわばりをほぐし、血行を整えることで、自然な回復力を引き出す伝統的な療法です。肩こりや腰痛にも効果が期待できます。</p>
      </div>
      <div class="section">
        <h3>施術の流れ</h3>
        <p>問診で体調をお伺いした後、状態に合わせて施術を行います。終了後はご自宅でできるケアもご案内いたします。</p>
      </div>
      <div class="lower">
        <div class="texts">
          <div class="section">
            <h3>訪問マッサージ</h3>
            <p>通院が難しい方のご自宅へ伺い、施術いたします。お気軽にご相談ください。</p>
          </div>
          <div class="section">
            <h3>受付時間</h3>
            <p>平日 9:00〜19:00 ／ 土曜 9:00〜13:00　日曜・祝日休診</p>
          </div>
        </div>
        <div class="flower-photo" role="img" aria-label="黄色い花の写真"></div>
      </div>
    </section>
  </div>
</div>
</body>
</html>
```